Business Card for IT Support Company
Aide Nova
Business Card for IT Support Company - Information Technology
Creative Brief
Professional
Assistance Informatique 24/7
Tél. 0900 417 536
2.50 CHF/min de 8h à 22h et 3.50 CHF/min de 22h à 8h depuis le réseau fixe.
info@aide-nova.ch
http://www.aide-nova.ch
No specific name, this is only a hotline IT support number Business Card (phone number is in the title) in Address box, it's the rates on the Business Number. We will use brivopress . ch as the printing company, here are the exact size in mm they send to me: Business card Size is 85x55mm (But file dimension must be 91x61mm) Colors needs to be send in CMYK, minimum 200 dpi, maximum quality.
- Contrôle à distance PC/MAC - Support technique informatique - Formation / Consulting / Coaching - Infographie / Graphisme - Création de Site Web - Smartphone / Tablette

```html
<!DOCTYPE html>
<html lang="en">
<head>
<meta charset="utf-8">
<title>Aide Nova – Business Card</title>
<link rel="stylesheet" href="https://fonts.googleapis.com/css2?family=Arimo:wght@400;700&display=swap">
<style>
  :root {
    --backdrop: #d9d9d6;
    --card-white: #f4f4f4;
    --card-shade: #e2e2e2;
    --band-black: #111111;
    --edge-grey: #9a9a9a;
    --accent-red: #e02b2b;
    --text-dark: #2a2a2a;
    --text-grey: #6b6b6b;
  }
  html, body {
    margin: 0;
    width: 1200px;
    height: 901px;
    overflow: hidden;
    background: var(--backdrop);
  }
  .business-card {
    position: absolute;
    left: 100px;
    top: 127px;
    width: 1000px;
    height: 647px;
    border-radius: 40px;
    overflow: hidden;
    background: linear-gradient(160deg, var(--card-white) 0%, var(--card-white) 55%, var(--card-shade) 100%);
    box-shadow: 0 10px 30px rgba(0,0,0,0.18);
    font-family: "Arimo", Arial, sans-serif;
  }
  .card-shapes {
    position: absolute;
    inset: 0;
  }
  .brand-mark {
    position: absolute;
    left: 590px;
    top: 90px;
    width: 100px;
    height: 100px;
    border-radius: 50%;
    background: var(--accent-red);
  }
  .brand-name {
    position: absolute;
    left: 470px;
    top: 262px;
    margin: 0;
    font-size: 40px;
    font-weight: 700;
    color: var(--text-dark);
  }
  .call-label {
    position: absolute;
    left: 70px;
    top: 212px;
    margin: 0;
    font-size: 30px;
    font-weight: 700;
    letter-spacing: 1px;
    color: var(--accent-red);
  }
  .phone-number {
    position: absolute;
    left: 70px;
    top: 256px;
    margin: 0;
    font-size: 46px;
    font-weight: 700;
    letter-spacing: 5px;
    color: var(--text-grey);
  }
  .contact-line {
    position: absolute;
    left: 70px;
    margin: 0;
    font-size: 25px;
    font-weight: 700;
    letter-spacing: 3px;
    text-transform: uppercase;
    color: var(--text-grey);
  }
  .contact-email { top: 450px; }
  .contact-web { top: 500px; }
</style>
</head>
<body>
  <div class="business-card">
    <svg class="card-shapes" width="1000" height="647" viewBox="0 0 1000 647" aria-hidden="true">
      <path class="band-edge" d="M715,0 C885,60 965,300 945,647 L1000,647 L1000,0 Z" fill="var(--edge-grey)"/>
      <path class="band-black" d="M730,0 C900,60 980,300 960,647 L1000,647 L1000,0 Z" fill="var(--band-black)"/>
      <path class="band-red" d="M790,0 C900,20 965,65 1000,120 L1000,0 Z" fill="var(--accent-red)"/>
    </svg>

    <div class="brand-mark"></div>
    <p class="brand-name">Aide Nova 24/7</p>

    <p class="call-label">CALL US TODAY</p>
    <p class="phone-number">0900 417 536</p>

    <p class="contact-line contact-email">info@aide-nova.ch</p>
    <p class="contact-line contact-web">www.aide-nova.ch</p>
  </div>
</body>
</html>
```